Rosquillas de Maíz y Queso

Necesitamos el de una bolsa que sea parcialmente transparente, para este producto, nuestra empresa se llama TOVALSA (Comercial Tovalsa), estamos ubicados en Honduras. Este un producto típico de Honduras, Este producto es para consumo masivo y será vendido en supermercados.
Adjunto ejemplos de empaques de este producto ya existentes.
Updates

Es nuestra primera vez, y queremos revisar bien los diseños, adicionalmente unos nos llegaron ayer y queremos unos pequeños cambios para poder decidir. Gracias

Target Market(s)

Clientes en supermercados

Industry/Entity Type

Panaderia

Requirements
Must have
• La bolsa debe ser transparente con ventana para ver el producto
Nice to have
• Tiene que tener una ventana grande la bolsa o ser la mayor parte transparente para mostrar el producto

```html
<!DOCTYPE html>
<html lang="es">
<head>
<meta charset="utf-8">
<title>Rosquillas de queso – Tovalsa</title>
<link href="https://fonts.googleapis.com/css2?family=Lilita+One&family=Kaushan+Script&family=Roboto:wght@700;900&display=swap" rel="stylesheet">
<style>
  :root{
    --bg:#ffffff;
    --bag:#eceff2;
    --bag-seal:#f6f7f9;
    --bag-edge:#d3d7dc;
    --snack-light:#f0b64a;
    --snack-dark:#d48a1f;
    --label-teal:#1faf90;
    --frame-green:#0f6e42;
    --band-green:#0a5632;
    --gold:#d2ac52;
    --gold-light:#f2d98a;
    --pill:#f7b934;
    --ink:#1d2a22;
    --white:#ffffff;
  }
  html,body{margin:0;padding:0;overflow:hidden;background:var(--bg);}
  .canvas{width:945px;height:1200px;position:relative;overflow:hidden;background:var(--bg);}
  .package{position:absolute;inset:0;width:945px;height:1200px;display:block;}
  .brand-name{font-family:"Roboto",Arial,sans-serif;font-weight:900;font-size:34px;letter-spacing:2px;fill:var(--frame-green);}
  .product-name{font-family:"Lilita One","Arial Black",sans-serif;font-size:94px;fill:var(--white);}
  .product-flavor{font-family:"Kaushan Script",cursive;font-size:58px;fill:var(--band-green);}
  .quality-line{font-family:"Roboto",Arial,sans-serif;font-weight:700;font-size:13px;letter-spacing:2px;fill:var(--white);}
  .net-weight{font-family:"Roboto",Arial,sans-serif;font-weight:700;font-size:22px;fill:var(--ink);}
</style>
</head>
<body>
<div class="canvas">
  <svg class="package" viewBox="0 0 945 1200" xmlns="http://www.w3.org/2000/svg">
    <defs>
      <linearGradient id="snackTone" x1="0" y1="0" x2="1" y2="1">
        <stop offset="0" stop-color="var(--snack-light)"/>
        <stop offset="1" stop-color="var(--snack-dark)"/>
      </linearGradient>
      <linearGradient id="goldEdge" x1="0" y1="0" x2="1" y2="0">
        <stop offset="0" stop-color="var(--gold)"/>
        <stop offset=".5" stop-color="var(--gold-light)"/>
        <stop offset="1" stop-color="var(--gold)"/>
      </linearGradient>
      <path id="qualityArc" d="M425,790 A70,70 0 0 1 557,790"/>
    </defs>

    <g class="bag">
      <rect x="120" y="32" width="712" height="1148" rx="10" fill="var(--bag)" stroke="var(--bag-edge)" stroke-width="2"/>
      <rect class="bag-seal-top" x="120" y="32" width="712" height="62" fill="var(--bag-seal)"/>
      <rect class="bag-seal-bottom" x="120" y="1128" width="712" height="52" fill="var(--bag-seal)"/>
      <rect class="product-window" x="160" y="250" width="630" height="870" rx="120" fill="url(#snackTone)" opacity=".85"
            role="img" aria-label="Rosquillas de maíz y queso visibles a través de la bolsa transparente"/>
    </g>

    <g class="label">
      <path d="M288,352 A42,42 0 0 0 330,310 L652,310 A42,42 0 0 0 694,352 L694,994 L288,994 Z" fill="var(--frame-green)"/>
      <path d="M298,358 A40,40 0 0 0 336,320 L646,320 A40,40 0 0 0 684,358 L684,984 L298,984 Z" fill="none" stroke="var(--gold)" stroke-width="3"/>
      <path d="M304,362 A38,38 0 0 0 340,326 L642,326 A38,38 0 0 0 678,362 L678,978 L304,978 Z" fill="var(--label-teal)"/>

      <circle cx="392" cy="392" r="9" fill="var(--frame-green)"/>
      <text class="brand-name" x="500" y="404" text-anchor="middle">TOVALSA</text>

      <g class="ribbon" transform="rotate(-17 491 520)">
        <polygon points="244,455 260,455 260,572 232,562" fill="var(--band-green)"/>
        <rect x="258" y="450" width="466" height="120" fill="var(--band-green)"/>
        <rect x="258" y="443" width="466" height="7" fill="url(#goldEdge)"/>
        <rect x="258" y="570" width="466" height="7" fill="url(#goldEdge)"/>
        <text class="product-name" x="491" y="545" text-anchor="middle">Rosquillas</text>
        <text class="product-flavor" x="545" y="640" text-anchor="middle">de queso</text>
      </g>

      <text class="quality-line"><textPath href="#qualityArc" startOffset="50%" text-anchor="middle">PREMIUM QUALITY</textPath></text>
      <polygon class="crown" points="478,808 482,792 489,801 491,788 493,801 500,792 504,808" fill="var(--white)"/>

      <g class="free-from" fill="none" stroke="var(--ink)" stroke-width="2.5" opacity=".75">
        <circle cx="380" cy="848" r="19"/><line x1="367" y1="835" x2="393" y2="861"/>
        <circle cx="435" cy="848" r="19"/><line x1="422" y1="835" x2="448" y2="861"/>
        <circle cx="491" cy="848" r="19"/><line x1="478" y1="835" x2="504" y2="861"/>
        <circle cx="547" cy="848" r="19"/><line x1="534" y1="835" x2="560" y2="861"/>
        <circle cx="602" cy="848" r="19"/><line x1="589" y1="835" x2="615" y2="861"/>
      </g>

      <rect class="weight-pill" x="381" y="887" width="210" height="40" rx="20" fill="var(--pill)"/>
      <text class="net-weight" x="486" y="915" text-anchor="middle">Weight 240 g</text>
    </g>
  </svg>
</div>
</body>
</html>
```